Corvane Thinner Logo and Packaging Design

We are seeking a striking and professional logo and packaging design for our new product line, Corvane Thinner. This logo will be used on the packaging for three different sizes of half-transparent carboys: 1L, 4L, and 20L. Corvane Thinner is a high-quality solvent brand known for its excellent solvency, fast-drying properties, and pleasant smell. The logo should feature an eagle motif to symbolize power and precision, and our slogan, "FLY WITH QUALITY." The design should be suitable for placement on hardware store and warehouse shelves. Additionally, we need the designer to create an eagle logo to accompany the packaging.

Packaging Dimensions:
1L Carboy:
Front: 71mm height x 142mm width
Side: 71mm height x 73mm width
4L Carboy:
Front: 160mm height x 170mm width
Side: 160mm height x 120mm width
20L Carboy:
Front: 245mm height x 190mm width
Side: 215mm height x 190mm width
Front Label Requirements:

Product Name: Thinner QRZ
Volume: 20L
Precautionary Statements:
Keep Away from Sources of ignition - No Smoking
Avoid Contact with Eyes
Do Not Empty into Drains or Sewers
Take Precautionary Measures Against Static Discharge
Hazard Statements:
Flammable Liquid and Vapor
May be fatal if swallowed or enters Airways
Causes Skin Irritation
Causes Serious Eye Irritation
Causes Damage to Organs if Prolonged or Repeated Exposure
Hazard Pictograms: (Include relevant hazard symbols)
Design Requirements:

Logo: Eagle motif (to be designed by the designer)
Slogan: FLY WITH QUALITY
Color Scheme: Designer to recommend (should be striking and professional for retail display)

Please see my latest picture. Kindly note the packaging is in Plastic Carboy (not in metal tin as per PS).

Eagle to be more majestic and bigger (as if soaring in the sky).
Singapore landscape as background to have Singapore identity such as TKP, Lumora Wheel, orchid near the cove etc.
Updates

Eagle to be more majestic and bigger, wings to spread wide.
We not want it to be of photo style, but more on a cartoon style. Please see my latest file uploaded.

Target Market(s)

Our target market includes painting companies, construction companies, direct household consumers, and industrial users who require high-quality solvents for various applications.

Industry/Entity Type

Chemical, spray paint and painting, household, industrial

Requirements
Must have
• Professional and Striking Design: Eye-catching and professional packaging for retail shelves. Eagle Logo: A strong, precise eagle logo. Slogan: "FLY WITH QUALITY" prominently displayed. Clear Precautionary and Hazard Statements: Important safety information and pictograms. Volume Indication: Clearly marked (e.g., 1L, 4L, 20L). Eagle to be more majestic and bigger (as if soaring in the sky). Singapore landscape as background to have Singapore identity such as TKP, Lumora Wheel, orchid near the cove etc.
Nice to have
• Color Scheme Recommendations: Suggestions for a professional, striking color scheme. Versatility: Design elements adaptable across different sizes of packaging. Environmentally Friendly Elements: Indications of sustainability or eco-friendliness in the design.
Should not have
• Overly Complex Designs: Avoid cluttered or overly intricate designs that detract from readability. Inconsistent Branding: Ensure all elements are cohesive and align with the brand identity.

```html
<!DOCTYPE html>
<html lang="en">
<head>
<meta charset="utf-8">
<title>Corvane Thinner – Brand and Label Board</title>
<link href="https://fonts.googleapis.com/css2?family=Montserrat:wght@500;600;700;800;900&display=swap" rel="stylesheet">
<style>
  :root {
    --brand-yellow: #ebc120;
    --brand-black: #000000;
    --paper-white: #ffffff;
    --board-grey: #808080;
    --copy-dark: #3b3b3b;
    --hazard-red: #e30613;
  }
  * { margin: 0; padding: 0; box-sizing: border-box; }
  html, body { width: 800px; height: 1200px; overflow: hidden; }
  body { font-family: "Montserrat", sans-serif; background: var(--paper-white); }
  .board { position: relative; width: 800px; height: 1200px; }
  .panel { position: absolute; }
  .panel--yellow { left: 0; top: 0; width: 400px; height: 400px; background: var(--brand-yellow); }
  .panel--white { left: 400px; top: 0; width: 400px; height: 800px; background: var(--paper-white); }
  .panel--black { left: 0; top: 400px; width: 400px; height: 400px; background: var(--brand-black); }
  .panel--grey { left: 0; top: 800px; width: 800px; height: 400px; background: var(--board-grey); }

  .wordmark {
    position: absolute;
    display: flex; flex-direction: column; align-items: center;
    font-family: "Montserrat", sans-serif; font-weight: 900;
    text-transform: uppercase; line-height: 0.95; letter-spacing: 1px;
  }
  .wordmark__square { width: 46px; height: 46px; margin-bottom: 18px; }
  .wordmark__line { font-size: 44px; }
  .wordmark--on-yellow { color: var(--brand-black); }
  .wordmark--on-yellow .wordmark__square { background: var(--brand-black); }
  .wordmark--on-white, .wordmark--on-black { color: var(--brand-yellow); }
  .wordmark--on-white .wordmark__square, .wordmark--on-black .wordmark__square { background: var(--brand-yellow); }

  .label { position: absolute; display: block; }
  .label--20l { left: 494px; top: 468px; width: 211px; height: 273px; }
  .label--4l { left: 24px; top: 824px; width: 383px; height: 358px; }
  .label--1l { left: 449px; top: 921px; width: 318px; height: 159px; }

  .t-brand { font-weight: 900; fill: var(--brand-yellow); text-transform: uppercase; }
  .t-title { font-weight: 800; fill: var(--paper-white); }
  .t-grade { font-weight: 900; fill: var(--brand-yellow); }
  .t-heading { font-weight: 700; fill: var(--copy-dark); }
  .t-body { font-weight: 500; fill: var(--copy-dark); }
  .t-volume { font-weight: 900; fill: var(--brand-black); }
  .t-unit { font-weight: 500; fill: var(--brand-black); }
  .t-slogan { font-weight: 800; fill: var(--paper-white); }
  .sprite { position: absolute; width: 0; height: 0; }
</style>
</head>
<body>
<svg class="sprite" aria-hidden="true">
  <defs>
    <symbol id="picto-flame" viewBox="-50 -50 100 100">
      <rect x="-34" y="-34" width="68" height="68" transform="rotate(45)" fill="#fff" stroke="#e30613" stroke-width="7"/>
      <path d="M0 -24 C10 -12 16 -4 14 8 C12 16 6 20 0 20 C-8 20 -14 14 -14 6 C-14 -2 -8 -6 -6 -14 C-2 -8 2 -6 0 -24 Z" fill="#000"/>
      <rect x="-16" y="22" width="32" height="4" fill="#000"/>
    </symbol>
    <symbol id="picto-health" viewBox="-50 -50 100 100">
      <rect x="-34" y="-34" width="68" height="68" transform="rotate(45)" fill="#fff" stroke="#e30613" stroke-width="7"/>
      <circle cx="0" cy="-12" r="8" fill="#000"/>
      <path d="M-16 22 L-12 2 L0 -2 L12 2 L16 22 Z" fill="#000"/>
      <path d="M0 4 L3 10 L9 11 L4 15 L6 21 L0 18 L-6 21 L-4 15 L-9 11 L-3 10 Z" fill="#fff"/>
    </symbol>
    <symbol id="picto-exclaim" viewBox="-50 -50 100 100">
      <rect x="-34" y="-34" width="68" height="68" transform="rotate(45)" fill="#fff" stroke="#e30613" stroke-width="7"/>
      <path d="M-5 -26 L5 -26 L3 8 L-3 8 Z" fill="#000"/>
      <circle cx="0" cy="18" r="5" fill="#000"/>
    </symbol>
  </defs>
</svg>

<main class="board">
  <section class="panel panel--yellow">
    <div class="wordmark wordmark--on-yellow" style="left:0;width:400px;top:128px;">
      <span class="wordmark__square"></span>
      <span class="wordmark__line">Corvane</span>
      <span class="wordmark__line">Thinner</span>
    </div>
  </section>

  <section class="panel panel--white">
    <div class="wordmark wordmark--on-white" style="left:0;width:400px;top:105px;">
      <span class="wordmark__square"></span>
      <span class="wordmark__line">Corvane</span>
      <span class="wordmark__line">Thinner</span>
    </div>
  </section>

  <section class="panel panel--black">
    <div class="wordmark wordmark--on-black" style="left:0;width:400px;top:128px;">
      <span class="wordmark__square"></span>
      <span class="wordmark__line">Corvane</span>
      <span class="wordmark__line">Thinner</span>
    </div>
  </section>

  <section class="panel panel--grey"></section>

  <!-- 20 litre label -->
  <svg class="label label--20l" viewBox="0 0 415 535" aria-label="Thinner QRZ 20 litre label">
    <rect width="415" height="535" rx="22" fill="var(--brand-black)"/>
    <path d="M0 238 L195 135 L415 135 L415 513 Q415 535 393 535 L22 535 Q0 535 0 513 Z" fill="var(--brand-yellow)"/>
    <path d="M0 465 L345 465 L412 535 L22 535 Q0 535 0 513 Z" fill="var(--brand-black)"/>
    <rect x="54" y="44" width="26" height="26" fill="var(--brand-yellow)"/>
    <text class="t-brand" x="68" y="108" font-size="24" text-anchor="middle">CORVANE</text>
    <text class="t-brand" x="68" y="132" font-size="24" text-anchor="middle">THINNER</text>
    <text class="t-title" x="388" y="58" font-size="38" text-anchor="end">THINNER</text>
    <text class="t-grade" x="400" y="132" font-size="80" text-anchor="end">QRZ</text>
    <text class="t-heading" x="160" y="188" font-size="21">Precautionary</text>
    <g class="t-body" font-size="8.5">
      <text x="160" y="203">Keep Away from Sources of ignition - No Smoking</text>
      <text x="160" y="215">Avoid Contact with Eyes</text>
      <text x="160" y="228">Do Not Empty into Drains or Sewers</text>
      <text x="160" y="240" textLength="236" lengthAdjust="spacingAndGlyphs">Take Precautionary Measures Against Static Discharge</text>
    </g>
    <text class="t-heading" x="160" y="283" font-size="21">Hazards</text>
    <g class="t-body" font-size="8.5">
      <text x="160" y="299">Flammable Liquid and Vapor</text>
      <text x="160" y="311">May be fatal if swallowed or enters Airways</text>
      <text x="160" y="324">Causes Skin Irritation</text>
      <text x="160" y="336">Causes Serious Eye Irritation</text>
      <text x="160" y="349">Causes Damage to Organs if Prolonged</text>
      <text x="160" y="361">or Repeated Exposure</text>
    </g>
    <text class="t-volume" x="70" y="320" font-size="68" text-anchor="middle">20</text>
    <text class="t-unit" x="70" y="350" font-size="27" text-anchor="middle">LITRES</text>
    <use href="#picto-flame" x="165" y="387" width="54" height="54"/>
    <use href="#picto-health" x="232" y="387" width="54" height="54"/>
    <use href="#picto-exclaim" x="299" y="387" width="54" height="54"/>
    <text class="t-slogan" x="22" y="512" font-size="31">FLY WITH QUALITY</text>
  </svg>

  <!-- 4 litre label -->
  <svg class="label label--4l" viewBox="0 0 749 702" aria-label="Thinner QRZ 4 litre label">
    <rect width="749" height="702" rx="40" fill="var(--brand-black)"/>
    <path d="M0 410 L352 228 L749 228 L749 662 Q749 702 709 702 L40 702 Q0 702 0 662 Z" fill="var(--brand-yellow)"/>
    <path d="M0 617 L365 617 L459 702 L40 702 Q0 702 0 662 Z" fill="var(--brand-black)"/>
    <rect x="100" y="70" width="46" height="46" fill="var(--brand-yellow)"/>
    <text class="t-brand" x="123" y="190" font-size="42" text-anchor="middle">CORVANE</text>
    <text class="t-brand" x="123" y="234" font-size="42" text-anchor="middle">THINNER</text>
    <text class="t-title" x="700" y="88" font-size="72" text-anchor="end">THINNER</text>
    <text class="t-grade" x="725" y="226" font-size="144" text-anchor="end">QRZ</text>
    <text class="t-heading" x="345" y="300" font-size="36">Precautionary</text>
    <g class="t-body" font-size="15">
      <text x="346" y="328">Keep Away from Sources of ignition - No Smoking</text>
      <text x="346" y="348">Avoid Contact with Eyes</text>
      <text x="346" y="368">Do Not Empty into Drains or Sewers</text>
      <text x="346" y="388" textLength="380" lengthAdjust="spacingAndGlyphs">Take Precautionary Measures Against Static Discharge</text>
    </g>
    <text class="t-heading" x="345" y="455" font-size="36">Hazards</text>
    <g class="t-body" font-size="15">
      <text x="346" y="483">Flammable Liquid and Vapor</text>
      <text x="346" y="503">May be fatal if swallowed or enters Airways</text>
      <text x="346" y="523">Causes Skin Irritation</text>
      <text x="346" y="543">Causes Serious Eye Irritation</text>
      <text x="346" y="563">Causes Damage to Organs if Prolonged</text>
      <text x="346" y="583">or Repeated Exposure</text>
    </g>
    <text class="t-volume" x="130" y="520" font-size="130" text-anchor="middle">4</text>
    <text class="t-unit" x="130" y="578" font-size="52" text-anchor="middle">LITRES</text>
    <use href="#picto-flame" x="440" y="606" width="84" height="84"/>
    <use href="#picto-health" x="530" y="606" width="84" height="84"/>
    <use href="#picto-exclaim" x="620" y="606" width="84" height="84"/>
    <text class="t-slogan" x="22" y="672" font-size="34">FLY WITH QUALITY</text>
  </svg>

  <!-- 1 litre label -->
  <svg class="label label--1l" viewBox="0 0 624 312" aria-label="Thinner QRZ 1 litre label">
    <rect width="624" height="312" rx="18" fill="var(--brand-black)"/>
    <path d="M0 177 L330 98 L624 98 L624 294 Q624 312 606 312 L18 312 Q0 312 0 294 Z" fill="var(--brand-yellow)"/>
    <path d="M308 312 L355 262 L624 262 L624 294 Q624 312 606 312 Z" fill="var(--brand-black)"/>
    <rect x="50" y="30" width="22" height="22" fill="var(--brand-yellow)"/>
    <text class="t-brand" x="61" y="82" font-size="19" text-anchor="middle">CORVANE</text>
    <text class="t-brand" x="61" y="102" font-size="19" text-anchor="middle">THINNER</text>
    <text class="t-title" x="150" y="94" font-size="46">THINNER</text>
    <text class="t-grade" x="612" y="98" font-size="88" text-anchor="end">QRZ</text>
    <text class="t-heading" x="140" y="145" font-size="21">Precautionary</text>
    <g class="t-body" font-size="8.5">
      <text x="141" y="162">Keep Away from Sources of ignition - No Smoking</text>
      <text x="141" y="175">Avoid Contact with Eyes</text>
      <text x="141" y="188">Do Not Empty into Drains or Sewers</text>
      <text x="141" y="201" textLength="250" lengthAdjust="spacingAndGlyphs">Take Precautionary Measures Against Static Discharge</text>
    </g>
    <text class="t-heading" x="410" y="145" font-size="21">Hazards</text>
    <g class="t-body" font-size="8.5">
      <text x="411" y="162">Flammable Liquid and Vapor</text>
      <text x="411" y="175" textLength="200" lengthAdjust="spacingAndGlyphs">May be fatal if swallowed or enters Airways</text>
      <text x="411" y="188">Causes Skin Irritation</text>
      <text x="411" y="201">Causes Serious Eye Irritation</text>
      <text x="411" y="214">Causes Damage to Organs if Prolonged</text>
      <text x="411" y="227">or Repeated Exposure</text>
    </g>
    <text class="t-volume" x="68" y="236" font-size="80" text-anchor="middle">1</text>
    <text class="t-unit" x="68" y="284" font-size="29" text-anchor="middle">LITRES</text>
    <use href="#picto-flame" x="150" y="232" width="52" height="52"/>
    <use href="#picto-health" x="210" y="232" width="52" height="52"/>
    <use href="#picto-exclaim" x="270" y="232" width="52" height="52"/>
    <text class="t-slogan" x="362" y="298" font-size="23">FLY WITH QUALITY</text>
  </svg>
</main>
</body>
</html>
```